Financial Advisor Resource Firm needs business card design

Need business card design for company in Omaha NE called Tallowbrook Partners. We provide resources to financial advisors....workshop programs, retirement analysis, and insurance planning. I would like to see designs that use grays, greens, black, and white colors. The final design should communicate 'collaboration' and be simple yet attractive to financial planning clients. I will attached our logo and another picture of a puzzle piece coming together. I would like the incorporate the puzzle picture somehow, maybe on the back somehow, with color or just the gray scale....OR, the picture be the front of the card with 'Tallowbrook' definition on it (see upload) and then company logo, employee name, title, address on the back (see ppt uploaded). The following disclosure needs to be included somewhere- Advisory services offered through Marlowe Ridge Advisors, LLC.
Updates

I uploaded a svg and ai file of the logo

Target Market(s)

Financial planning clients and financial advisors....so pretty diverse age range of about 40-70.

Industry/Entity Type

Financial Planning

Contact Information for Business Card

Dennis K. Holloway, MBA
Founder/President
5727 E. Larkspur Avenue
Suite 418
Omaha, NE 68297
Phone- (402) 555-0147
Cell- (402) 555-0183
Fax- (402) 555-0129
email- dennis@tallowbrookgroup.example
web address- www.tallowbrookgroup.example

Colors
1b1b1b
474747
d3d3d3
ffffff
9bcb3c
abd036

Requirements
Must have
• Must include logo provided, must be 2 sided, and must have disclosure...all of these items listed in project description

```html
<!DOCTYPE html>
<html lang="en">
<head>
<meta charset="utf-8">
<title>Tallowbrook Partners — Business Card</title>
<link rel="stylesheet" href="https://fonts.googleapis.com/css2?family=Source+Sans+3:wght@400;600&display=swap">
<style>
  :root {
    --ink: #1b1b1b;
    --graphite: #474747;
    --silver: #d3d3d3;
    --white: #ffffff;
    --leaf: #9bcb3c;
    --lime: #abd036;
    --stage: #7a7a7a;
    --muted: #a9a9a9;
    --fine: #8a8a8a;
  }
  * { margin: 0; padding: 0; box-sizing: border-box; }
  html, body { width: 1200px; height: 800px; overflow: hidden; }
  body {
    position: relative;
    background: var(--stage);
    font-family: "Source Sans 3", sans-serif;
  }

  .card {
    position: absolute;
    width: 480px;
    height: 320px;
    overflow: hidden;
  }

  /* Front */
  .card-front { left: 105px; top: 73px; }
  .front-photo {
    position: absolute; inset: 0;
    background: radial-gradient(ellipse at 62% 58%, #c9c9c9 0%, #8d8d8d 35%, #4a4a4a 70%, #2a2a2a 100%);
  }
  .front-logo-plate {
    position: absolute;
    left: 270px; top: 67px;
    width: 190px; height: 45px;
    background: var(--white);
    border-radius: 8px 0 0 8px;
    display: flex; align-items: center; justify-content: center; gap: 7px;
  }
  .brand-name {
    font-weight: 600;
    color: var(--ink);
    white-space: nowrap;
  }
  .front-logo-plate .brand-name { font-size: 16px; }
  .brand-dot {
    width: 9px; height: 9px; border-radius: 50%;
    background: var(--leaf);
    flex: none;
  }
  .front-definition {
    position: absolute;
    left: 40px; top: 271px;
    font-size: 12.5px;
    font-weight: 600;
    letter-spacing: 0.85px;
    color: var(--white);
    white-space: nowrap;
  }

  /* Back */
  .card-back { left: 585px; top: 412px; display: flex; }
  .back-details {
    width: 245px; height: 100%;
    background: linear-gradient(180deg, #2b2b2b 0%, var(--ink) 100%);
    padding: 83px 0 0 28px;
    position: relative;
  }
  .holder-name {
    font-size: 16.4px;
    font-weight: 400;
    letter-spacing: 0.3px;
    color: var(--lime);
    white-space: nowrap;
  }
  .holder-title {
    font-size: 10px;
    color: var(--muted);
    margin-top: 2px;
  }
  .details-rule {
    position: absolute;
    left: 0; right: 0; top: 135px;
    height: 1px;
    background: var(--graphite);
  }
  .contact-list {
    list-style: none;
    position: absolute;
    left: 28px; top: 153px;
  }
  .contact-list li {
    display: flex; align-items: center;
    height: 17.7px;
    font-size: 9.5px;
    color: var(--silver);
    white-space: nowrap;
  }
  .contact-icon {
    width: 10px; height: 10px;
    margin-right: 16px;
    fill: var(--silver);
    flex: none;
  }
  .contact-icon.globe { fill: none; stroke: var(--silver); stroke-width: 0.9; }
  .contact-list .no-icon { padding-left: 26px; }
  .back-brand {
    flex: 1;
    background: var(--white);
    position: relative;
    display: flex; align-items: center; justify-content: center; gap: 8px;
  }
  .back-brand .brand-name { font-size: 18px; }
  .disclosure {
    position: absolute;
    left: 0; right: 0; bottom: 14px;
    text-align: center;
    font-size: 6.5px;
    color: var(--fine);
    white-space: nowrap;
  }
</style>
</head>
<body>

<section class="card card-front">
  <div class="front-photo" role="img" aria-label="Grayscale photo of several hands fitting puzzle pieces together"></div>
  <div class="front-logo-plate">
    <span class="brand-dot"></span>
    <span class="brand-name">Tallowbrook Partners</span>
  </div>
  <p class="front-definition">TO COME TOGETHER AND UNITE IN COMMON INTEREST AND FOCUS</p>
</section>

<section class="card card-back">
  <div class="back-details">
    <h1 class="holder-name">DENNIS K. HOLLOWAY, MBA</h1>
    <p class="holder-title">Founder/President</p>
    <div class="details-rule"></div>
    <ul class="contact-list">
      <li><svg class="contact-icon" viewBox="0 0 10 10"><path d="M5 1 0.5 5H2v4h2.2V6.5h1.6V9H8V5h1.5z"/></svg>5727 E. Larkspur Avenue</li>
      <li class="no-icon">Suite 418</li>
      <li class="no-icon">Omaha, NE 68297</li>
      <li><svg class="contact-icon" viewBox="0 0 10 10"><path d="M2 0.8 3.6 2.6 2.8 3.8C3.4 5 4.6 6.4 6 7.1L7.2 6.3 9 8 8 9.3C4.6 9 1 5.4 0.7 2z"/></svg>(402) 555-0147</li>
      <li><svg class="contact-icon" viewBox="0 0 10 10"><path d="M3 0.5h4a.7.7 0 0 1 .7.7v7.6a.7.7 0 0 1-.7.7H3a.7.7 0 0 1-.7-.7V1.2A.7.7 0 0 1 3 .5zM3.3 1.6v5.9h3.4V1.6zM5 8a.5.5 0 1 0 0 1 .5.5 0 0 0 0-1z"/></svg>(402) 555-0183</li>
      <li><svg class="contact-icon" viewBox="0 0 10 10"><path d="M2.5 1h4l1 1v2H2.5zM.5 4.5h9V9h-9zM2 5.7v1h3v-1z"/></svg>(402) 555-0129</li>
      <li><svg class="contact-icon" viewBox="0 0 10 10"><path d="M.5 2h9v.6L5 5.5.5 2.6zM.5 3.7 5 6.6l4.5-2.9V8.5h-9z"/></svg>dennis@tallowbrookgroup.example</li>
      <li><svg class="contact-icon globe" viewBox="0 0 10 10"><circle cx="5" cy="5" r="4.3"/><ellipse cx="5" cy="5" rx="1.9" ry="4.3"/><path d="M.7 5h8.6M1.4 2.8h7.2M1.4 7.2h7.2"/></svg>www.tallowbrookgroup.example</li>
    </ul>
  </div>
  <div class="back-brand">
    <span class="brand-dot"></span>
    <span class="brand-name">Tallowbrook Partners</span>
    <p class="disclosure">Advisory services offered through Marlowe Ridge Advisors, LLC</p>
  </div>
</section>

</body>
</html>
```